Hi we have a company called Brenlock Protection Services and are looking for a new design we are wanting flames as the last card was great with the whole background flames but you cant really see the services offered, phone, names etc.

We need something more upmarket and professional and only have a small budget

We need the words Brenlock Protection Services, Martin Pevelle MAQSrT - Fire Safety Consultant, Phone No 0492365140 address : PO Box 8362 TWRL 4183 ABN 71836205947, NRTW Lic.5742816 Email martin@brenlockgroup.com.au

Industry/Entity Type

Fire Safety

Font styles to use
Sans Serif

Colors
ec2027
ffc214

```html
<!DOCTYPE html>
<html lang="en">
<head>
<meta charset="UTF-8">
<title>Brenlock Protection Services – Business Card</title>
<link rel="stylesheet" href="https://fonts.googleapis.com/css2?family=Jost:wght@400;500&display=swap">
<style>
  :root {
    --backdrop: #d2d2d2;
    --card-black: #000000;
    --brand-gold: #ffc214;
    --brand-red: #ec2027;
  }
  * { margin: 0; padding: 0; box-sizing: border-box; }
  html, body {
    width: 1200px;
    height: 800px;
    overflow: hidden;
    background: var(--backdrop);
    font-family: "Jost", "Helvetica Neue", Arial, sans-serif;
  }
  .business-card {
    position: absolute;
    left: 100px;
    top: 114px;
    width: 1000px;
    height: 571px;
    background: var(--card-black);
    color: var(--brand-gold);
  }
  .company-name {
    position: absolute;
    left: 51px;
    top: 60px;
    font-size: 32px;
    font-weight: 500;
    letter-spacing: 0.3px;
    text-transform: uppercase;
    white-space: nowrap;
  }
  .consultant {
    position: absolute;
    left: 51px;
    top: 381px;
  }
  .consultant-name {
    font-size: 28px;
    font-weight: 400;
    line-height: 1.2;
    white-space: nowrap;
  }
  .consultant-role {
    font-size: 17px;
    font-weight: 400;
    line-height: 1.2;
  }
  .divider {
    position: absolute;
    left: 465px;
    top: 319px;
    width: 2px;
    height: 191px;
    background: var(--brand-gold);
  }
  .contact-list {
    position: absolute;
    left: 519px;
    top: 340px;
    list-style: none;
  }
  .contact-item {
    display: flex;
    align-items: center;
    height: 33.5px;
    font-size: 21px;
    font-weight: 400;
    white-space: nowrap;
  }
  .contact-icon {
    width: 22px;
    height: 22px;
    margin-right: 23px;
    flex: none;
  }
</style>
</head>
<body>
  <section class="business-card">
    <h1 class="company-name">Brenlock Protection Services</h1>

    <div class="consultant">
      <p class="consultant-name">Martin Pevelle MAQSrT</p>
      <p class="consultant-role">Fire Safety Consultant</p>
    </div>

    <div class="divider"></div>

    <ul class="contact-list">
      <li class="contact-item">
        <svg class="contact-icon" viewBox="0 0 22 22" aria-hidden="true">
          <rect width="22" height="22" rx="2" fill="#ffc214"/>
          <path d="M4 9 Q11 4 18 9 L16 11 L13.5 9.5 L13.5 8 Q11 7.2 8.5 8 L8.5 9.5 L6 11 Z" fill="#000"/>
          <rect x="6" y="12" width="10" height="5" rx="1" fill="#000"/>
        </svg>
        0492365140
      </li>
      <li class="contact-item">
        <svg class="contact-icon" viewBox="0 0 22 22" aria-hidden="true">
          <rect width="22" height="22" rx="2" fill="#ffc214"/>
          <rect x="4" y="6" width="14" height="10" fill="none" stroke="#000" stroke-width="1.6"/>
          <path d="M4 6 L11 12 L18 6 M4 16 L9 11 M18 16 L13 11" fill="none" stroke="#000" stroke-width="1.4"/>
        </svg>
        martin@brenlockgroup.com.au
      </li>
      <li class="contact-item">
        <svg class="contact-icon" viewBox="0 0 22 22" aria-hidden="true">
          <rect width="22" height="22" rx="2" fill="#ffc214"/>
          <path d="M11 4 A5 5 0 0 1 16 9 C16 12.5 11 18 11 18 C11 18 6 12.5 6 9 A5 5 0 0 1 11 4 Z" fill="#000"/>
          <circle cx="11" cy="9" r="2" fill="#ffc214"/>
        </svg>
        PO Box 8362 TWRL 4183
      </li>
      <li class="contact-item">
        <svg class="contact-icon" viewBox="0 0 22 22" aria-hidden="true">
          <rect width="22" height="22" rx="2" fill="#ffc214"/>
          <circle cx="11" cy="11" r="7" fill="#000"/>
          <circle cx="11.6" cy="7.6" r="1.1" fill="#ffc214"/>
          <path d="M10 10 L12 10 L11 15 L9.6 15 Z" fill="#ffc214"/>
        </svg>
        ABN 71836205947, NRTW Lic.5742816
      </li>
    </ul>
  </section>
</body>
</html>
```